依頼詳細
商品は布マスクになりますが、取り急ぎ添付の不織布マスクの内容で構いせん。
全体のイメージで決定したいと思います。
決定後に布マスクの詳細をお伝えしますので、完成品に仕上げて頂きたいと思います。

製品形状はPP袋(PPのベースは透明もしくはアルミ銀)
袋サイズ:W130xH180mm+ヘッダー部分H20mm

印刷は4色分解でも構いませんが、中国印刷の為、あまり複雑過ぎない程度の色使いでお願いします。

急ぎ提案なのでイメージだけでも早く提案してもらえば助かります。
説明不足で申し訳ございませんが、不明点はご連絡お願い致します。
記載項目
PP袋(PPのベースは透明もしくはアルミ銀)

印刷は4色分解でも構いませんが、中国グラビア印刷(8色まで)の為、あまり複雑過ぎない程度の色使いでお願いします。版代のコストも抑えたいです。
希望イメージ
シンプル 複雑
単色 カラフル
暗い 明るい
日常 高級
遊び心 厳粛
未来的 伝統的
女性的 男性的
希望する色
青系、水色系、無彩色系
納品ファイル
• イラストレーター形式 (.ai)
補足説明

お客様の選定により

たくさんのご提案ありがとうございました
またの機会にも是非またご提案お願い致します。

```html
<!DOCTYPE html>
<html lang="ja">
<head>
<meta charset="utf-8">
<title>高性能 布マスク パッケージ</title>
<link rel="stylesheet" href="https://fonts.googleapis.com/css2?family=Noto+Sans+JP:wght@400;500;700;900&display=swap">
<style>
  :root {
    --blue-deep: #0a3f9a;
    --blue-main: #1565c8;
    --blue-mid: #2f8be0;
    --blue-light: #7fc4f2;
    --sky: #d9efff;
    --white: #ffffff;
    --red: #e4162b;
    --yellow: #ffe23a;
    --text-dark: #1b2a4a;
  }
  * { margin: 0; padding: 0; box-sizing: border-box; }
  html, body { width: 813px; height: 1200px; overflow: hidden; background: #ffffff; }
  body { font-family: "Noto Sans JP", sans-serif; color: var(--text-dark); }

  .package {
    position: relative;
    width: 813px; height: 1200px;
    background: linear-gradient(180deg, var(--blue-main) 0%, var(--blue-mid) 45%, var(--blue-main) 75%, var(--blue-deep) 100%);
    overflow: hidden;
  }

  /* header band */
  .header-band {
    position: absolute; left: 0; top: 0; width: 813px; height: 214px;
    background: var(--white);
  }
  .header-title {
    position: absolute; left: 14px; top: 14px; width: 310px; height: 134px;
    background: var(--blue-main); border-radius: 10px;
    color: var(--white); white-space: nowrap;
  }
  .header-title .small-lead {
    position: absolute; left: 10px; top: 12px; width: 28px;
    font-size: 24px; font-weight: 900; line-height: 1.05; text-align: center;
  }
  .header-title .big {
    position: absolute; left: 44px; top: 4px;
    font-size: 58px; font-weight: 900; letter-spacing: -2px; line-height: 1.3;
  }
  .header-title .en {
    position: absolute; left: 12px; top: 98px;
    font-size: 16px; font-weight: 500; letter-spacing: 0.3px;
  }
  .tag-disposable {
    position: absolute; background: var(--red); color: var(--white);
    font-weight: 900; text-align: center; border-radius: 4px; white-space: nowrap;
  }
  .header-title .tag-disposable {
    left: 276px; top: 8px; width: 28px; height: 84px;
    writing-mode: vertical-rl; font-size: 17px; line-height: 28px;
  }

  .filter-label {
    position: absolute; left: 336px; top: 14px; width: 224px; height: 134px;
    background: var(--blue-light); border-radius: 10px;
    color: var(--white); text-align: center; white-space: nowrap;
    font-weight: 900; padding-top: 16px;
  }
  .filter-label .l1 { font-size: 40px; line-height: 1.2; }
  .filter-label .l2 { font-size: 28px; line-height: 1.4; }
  .size-label {
    position: absolute; left: 572px; top: 14px; width: 226px; height: 134px;
    background: var(--blue-main); border-radius: 10px; color: var(--white); text-align: center;
    padding-top: 10px;
  }
  .size-label .adult { font-size: 44px; font-weight: 900; line-height: 1.1; }
  .size-label .normal { display: inline-block; margin-top: 4px; background: var(--white); color: var(--blue-main); font-size: 19px; font-weight: 700; padding: 0 18px; border-radius: 4px; }
  .size-label .dim { font-size: 14px; margin-top: 4px; }

  .lead-copy {
    position: absolute; left: 24px; top: 156px; width: 770px;
    font-size: 16px; font-weight: 500; line-height: 1.5; color: var(--blue-deep);
  }

  /* main title */
  .main-title {
    position: absolute; left: 22px; top: 232px; width: 769px; height: 180px;
    background: var(--white); border-radius: 24px;
  }
  .main-title .stack {
    position: absolute; left: 20px; top: 14px; width: 100px; height: 152px;
    background: var(--blue-main); color: var(--white); border-radius: 10px;
    font-size: 40px; font-weight: 900; line-height: 1.15; text-align: center; padding-top: 8px;
  }
  .main-title .big {
    position: absolute; left: 132px; top: 8px; white-space: nowrap;
    font-size: 132px; font-weight: 900; letter-spacing: -5px; color: var(--blue-main); line-height: 1.15;
  }
  .main-title .tag-disposable { left: 656px; top: 14px; width: 96px; height: 152px; font-size: 40px; line-height: 1.15; padding-top: 26px; }
  .main-en {
    position: absolute; left: 0; width: 813px; text-align: center; top: 420px;
    font-size: 34px; font-weight: 700; color: var(--white); letter-spacing: 1px;
  }

  /* product visual */
  .mask-visual {
    position: absolute; left: 40px; top: 480px; width: 560px; height: 250px;
    border-radius: 40px;
    background: radial-gradient(ellipse at 45% 50%, #ffffff 0%, #eaf5ff 45%, rgba(160,210,245,0.35) 75%, rgba(160,210,245,0) 100%);
  }
  .callout {
    position: absolute; font-size: 15px; font-weight: 700; color: var(--white); line-height: 1.3;
  }
  .callout.on-light { color: var(--blue-deep); }
  .filter-badge {
    position: absolute; left: 540px; top: 600px; width: 250px; height: 100px;
  }
  .filter-badge .title {
    position: absolute; left: 0; top: 0; width: 250px; text-align: center;
    font-size: 40px; font-weight: 900; color: var(--white); line-height: 1.15;
  }
  .filter-visual {
    position: absolute; left: 565px; top: 710px; width: 210px; height: 130px;
    border-radius: 12px;
    background: linear-gradient(135deg, #ffffff 0%, #cfe8fb 60%, #9dcdf2 100%);
  }

  /* performance */
  .cut-box {
    position: absolute; left: 22px; top: 830px; width: 300px; height: 110px;
    background: var(--blue-deep); border-radius: 10px; color: var(--white); padding: 6px 12px;
  }
  .cut-box .pct { font-size: 42px; font-weight: 900; color: var(--yellow); line-height: 1.05; }
  .cut-box .pct small { font-size: 24px; }
  .cut-box .line { font-size: 21px; font-weight: 700; line-height: 1.3; }
  .cut-box .line.medical { font-size: 19px; color: var(--yellow); }
  .spec-list {
    position: absolute; left: 340px; top: 850px; width: 240px; list-style: none;
    font-size: 14px; font-weight: 500; color: var(--white); line-height: 1.7;
  }
  .spec-list b { font-weight: 900; }

  /* protection icons */
  .icon-row { position: absolute; left: 22px; top: 955px; display: flex; gap: 12px; }
  .icon-item { width: 130px; text-align: center; color: var(--white); font-size: 20px; font-weight: 700; }
  .icon-item svg { display: block; margin: 0 auto 4px; }

  .count-box {
    position: absolute; left: 610px; top: 960px; width: 180px; height: 70px;
    background: var(--white); border-radius: 10px; color: var(--blue-main);
    font-size: 44px; font-weight: 900; text-align: center; line-height: 70px;
  }
  .origin {
    position: absolute; left: 600px; top: 1036px; width: 200px; text-align: center;
    font-size: 28px; font-weight: 900; color: var(--white);
  }

  .notes {
    position: absolute; left: 22px; top: 1090px; width: 769px;
    font-size: 13px; line-height: 1.6; color: var(--white);
  }
</style>
</head>
<body>
<main class="package">
  <section class="header-band">
    <div class="header-title">
      <div class="small-lead">高性能</div>
      <div class="big">布マスク</div>
      <div class="en">High-Performance Cloth mask</div>
      <div class="tag-disposable">使い切り</div>
    </div>
    <div class="filter-label"><div class="l1">3層構造</div><div class="l2">フィルター採用</div></div>
    <div class="size-label">
      <div class="adult">大人用</div>
      <div class="normal">普通サイズ</div>
      <div class="dim">約175mm×90mm</div>
    </div>
    <p class="lead-copy">ウイルス、細菌、花粉、ホコリ等の侵入をブロックする3層構造フィルター採用。<br>日常生活の抗菌・防臭・消臭対策にも効果を発揮します。</p>
  </section>

  <section class="main-title">
    <div class="stack">高<br>性<br>能</div>
    <div class="big">布マスク</div>
    <div class="tag-disposable">使い<br>切り</div>
  </section>
  <p class="main-en">High-Performance Cloth mask</p>

  <div class="mask-visual" role="img" aria-label="白いプリーツ型マスクの製品イラスト"></div>
  <p class="callout on-light" style="left:420px; top:560px;">ノーズフィットで<br>ぴったりフィット</p>
  <p class="callout" style="left:640px; top:520px;">耳が痛くなりにくい<br>ソフトなゴム採用。</p>
  <p class="callout" style="left:60px; top:740px;">三段プリーツ構造。</p>

  <div class="filter-badge"><div class="title">3層構造<br>フィルター</div></div>
  <div class="filter-visual" role="img" aria-label="3層構造フィルターの断面イラスト"></div>

  <section class="cut-box">
    <div class="pct">99<small>%</small><span class="line"> カット</span></div>
    <div class="line">フィルターを採用</div>
    <div class="line medical">[医療用レベルのマスク]</div>
  </section>
  <ul class="spec-list">
    <li><b>VFE</b>(ウイルス飛沫の透過効率)</li>
    <li><b>BFE</b>(細菌の透過効率 3µm)</li>
    <li><b>PFE</b>(微粒子の透過効率 0.1µm)</li>
  </ul>

  <section class="icon-row">
    <div class="icon-item"><svg width="80" height="80" viewBox="0 0 80 80"><circle cx="40" cy="40" r="38" fill="#ffffff" opacity="0.9"/></svg>風邪</div>
    <div class="icon-item"><svg width="80" height="80" viewBox="0 0 80 80"><circle cx="40" cy="40" r="38" fill="#ffffff" opacity="0.9"/></svg>花粉</div>
    <div class="icon-item"><svg width="80" height="80" viewBox="0 0 80 80"><circle cx="40" cy="40" r="38" fill="#ffffff" opacity="0.9"/></svg>ウイルス</div>
    <div class="icon-item"><svg width="80" height="80" viewBox="0 0 80 80"><circle cx="40" cy="40" r="38" fill="#ffffff" opacity="0.9"/></svg>PM2.5</div>
  </section>

  <div class="count-box">3枚入</div>
  <div class="origin">日本製素材</div>

  <p class="notes">※注意：ウイルス感染、ハウスダスト、PM2.5を完全に防ぐものではありません。<br>※本品は使い捨てです。洗濯しての再使用はできません。肌に異常を感じた場合は使用を中止してください。<br>※乳幼児の手の届かない、直射日光を避けた場所に保管してください。</p>
</main>
</body>
</html>
```